Psychotherapy Practice Needs Non-Corporate Stationary

I need an elegant design for letterhead, envelope, and note card for my psychotherapy private practice in Silicon Valley. I work with pre-teens, teens, and adults primarily with anxiety, stress, and depression.

Stationary should convey warmth and professionalism. I tend to like somewhat modern designs.

My business card is already done--attached here for reference.

Target Market(s)

Professionals of Silicon Valley, Academic Advisors at High Schools, Psychologists, Psychiatrists, Pediatricians, Directors of Human Resources, Community leaders

Industry/Entity Type

Psychology

Font styles to use
Serif

Requirements
Must have
• Logo attached--can use with or without the name included. Feel free to move the name to the right of the logo. I included all versions just in case. Colors to use should match or go with the logo (greens, maybe blues if they go), but can be somewhat softer than the bold greens and browns used. (Ex. more sage green vs. kelly green)
• Letterhead--please include the following:
• Marisol Quenneville, LMFT
• 318 Bellweather Lane, Suite 15
• Palo Alto, CA 94317
• 650-555-0187
• marisol@marisolquenneville.example
• marisolquenneville.example
• Envelope--please include:
• Marisol Quenneville, LMFT
• Palo Alto, CA 94317
• 650-555-0187
• marisolquenneville.example
• Note Card--please include:
• Marisol Quenneville, LMFT
• 650-555-0187
• marisolquenneville.example
Nice to have
• I'd love to see examples both with and without a logo watermark in the background. I especially like the watermark towards the lower right corner for the letterhead. I'd also like to see some versions of the letterhead with all contact info at the bottom.
Should not have
• It should not be corporate and should avoid harsh lines.

```html
<!DOCTYPE html>
<html lang="en">
<head>
<meta charset="utf-8">
<title>Marisol Quenneville, LMFT — Stationery</title>
<link href="https://fonts.googleapis.com/css2?family=Marcellus+SC&family=PT+Sans:wght@400;700&display=swap" rel="stylesheet">
<style>
  :root {
    --bg: #e4e3df;
    --paper: #dededd;
    --ink: #2b2b2b;
    --brown: #2f2a1c;
    --green-deep: #2e8b3e;
    --green-soft: #7ab648;
    --leaf: #5a9a44;
    --mist: rgba(150, 165, 150, 0.16);
  }
  * { box-sizing: border-box; margin: 0; padding: 0; }
  html, body { width: 1200px; height: 829px; overflow: hidden; background: var(--bg); }
  body { position: relative; font-family: "PT Sans", sans-serif; color: var(--ink); }

  .sheet { position: absolute; background: var(--paper); overflow: hidden; }
  .brand-name { font-family: "Marcellus SC", serif; color: var(--ink); white-space: nowrap; }
  .brand-dot { display: block; border-radius: 50%; background: var(--leaf); }
  .band { position: absolute; left: 0; right: 0; bottom: 0; height: 7px; background: var(--brown); }
  .band svg { position: absolute; top: 0; height: 7px; }
  .watermark { position: absolute; border-radius: 50%;
    background: radial-gradient(circle, var(--mist) 0%, rgba(150,165,150,0.08) 55%, rgba(150,165,150,0) 72%); }
  .contact { font-size: 8.4px; line-height: 12px; }
  .contact strong { font-weight: 700; }
  .contact .icon-row { display: flex; align-items: center; gap: 5px; }
  .contact svg { width: 8px; height: 8px; fill: var(--ink); }

  /* Letterhead */
  .letterhead { left: 54px; top: 53px; width: 496px; height: 700px; }
  .letterhead .brand { position: absolute; left: 39px; top: 32px; width: 130px; text-align: center; }
  .letterhead .brand-dot { width: 54px; height: 54px; margin: 0 auto 8px; }
  .letterhead .brand-name { font-size: 11px; }
  .letterhead .contact { position: absolute; left: 326px; top: 39px; }
  .letterhead .contact .gap { height: 8px; }
  .letter { position: absolute; left: 36px; top: 220px; width: 462px; font-size: 8.6px; line-height: 11px; }
  .letter p { margin-bottom: 10px; }
  .letter .salutation { margin-bottom: 20px; }
  .letter .sign-off { margin-top: 18px; line-height: 12px; }
  .signature { position: absolute; left: 112px; top: 298px; width: 72px; height: 26px; border-radius: 8px;
    background: linear-gradient(90deg, rgba(70,100,170,0.18), rgba(70,100,170,0.06)); }
  .letterhead .watermark { left: 200px; top: 200px; width: 300px; height: 420px; }
  .letterhead .site { position: absolute; left: 0; right: 0; bottom: 28px; text-align: center;
    font-size: 8.4px; letter-spacing: 1.6px; font-style: italic; }

  /* Envelope */
  .envelope { position: absolute; left: 333px; top: 343px; width: 508px; height: 312px; }
  .envelope .flap { position: absolute; left: 0; top: 0; width: 508px; height: 86px; }
  .envelope .flap-dot { position: absolute; left: 231px; top: 5px; width: 46px; height: 46px; }
  .envelope .body { left: 0; top: 85px; width: 508px; height: 227px; }
  .envelope .watermark { left: 300px; top: 10px; width: 230px; height: 230px; }
  .envelope .brand { position: absolute; left: 13px; top: 16px; width: 130px; text-align: center; }
  .envelope .brand-dot { width: 48px; height: 48px; margin: 0 auto 8px; }
  .envelope .brand-name { font-size: 9px; }
  .envelope .divider { position: absolute; left: 121px; top: 17px; width: 1px; height: 62px; background: #9a9a96; }
  .envelope .contact { position: absolute; left: 132px; top: 17px; font-size: 8px; line-height: 11.5px; }
  .envelope .contact .gap { height: 4px; }

  /* Note cards */
  .card { left: 875px; width: 240px; }
  .card-tent { top: 70px; height: 168px; }
  .card-tent .brand { position: absolute; left: 15px; top: 118px; display: flex; align-items: flex-end; gap: 4px; }
  .card-tent .brand-dot { width: 30px; height: 30px; }
  .card-tent .brand-name { font-size: 8px; margin-bottom: 2px; }
  .card-centered { top: 283px; height: 170px; }
  .card-centered .brand { position: absolute; left: 0; right: 0; top: 26px; text-align: center; }
  .card-centered .brand-dot { width: 24px; height: 24px; margin: 0 auto 4px; }
  .card-centered .brand-name { font-size: 5px; }
  .card-centered .site { position: absolute; left: 0; right: 0; bottom: 12px; text-align: center; font-size: 7px; color: #555; }
  .card-blank { top: 485px; height: 176px; }
</style>
</head>
<body>

<!-- Letterhead -->
<section class="sheet letterhead">
  <div class="watermark" role="img" aria-label="Faint tree watermark"></div>
  <div class="brand">
    <span class="brand-dot"></span>
    <span class="brand-name">Marisol Quenneville, LMFT</span>
  </div>
  <div class="contact">
    <strong>Marisol Quenneville, LMFT</strong><br>
    318 Bellweather Lane, Suite 15<br>
    Palo Alto, CA 94317
    <div class="gap"></div>
    <div class="icon-row"><svg viewBox="0 0 10 10"><path d="M1 3c0-1 1-2 4-2s4 1 4 2v1H7V3H3v1H1zM2 5h6l1 4H1z"/></svg>650-555-0187</div>
    <div class="icon-row"><svg viewBox="0 0 10 10"><path d="M0 2h10v6H0zM1 3l4 3 4-3"/></svg>marisol@marisolquenneville.example</div>
  </div>
  <div class="letter">
    <p class="salutation">Dear Mr. Hartley,</p>
    <p>Lorem ipsum dolor sit amet, consectetur adipiscing elit. Donec orci purus, luctus vitae dignissim eu, iaculis sed purus. Vivamus faucibus, ipsum nec aliquet viverra, leo mauris condimentum ligula, sit amet sagittis enim ligula quis arcu. Nam egestas tortor id nisi porttitor mattis. In tortor ante, ultricies in suscipit a, tempus non massa. Vivamus et auctor mi.</p>
    <p>Fusce vel massa nulla. Phasellus nec eros mauris, et scelerisque orci porta a id massa. Quisque accumsan iaculis magna sit amet fringilla semper, odio nibh rutrum mi, id feugiat ante nisi eu risus. Vestibulum in mi. Cras mattis varius eros, vel fringilla nisi suscipit eget.</p>
    <p>Quisque scelerisque sagittis nulla at porttitor. Mauris a justo et tellus euismod commodo aliquet a quam. Pellentesque arcu velit, cursus erat sem, rhoncus id ullamcorper vitae, rhoncus et arcu. In ultrices eu magna a metus ornare faucibus.</p>
    <p>Fusce aliquet faucibus ultricies. Morbi semper, est id tincidunt gravida nulla leo eu purus. Quisque nec diam sed risus consectetur a congue.</p>
    <div class="sign-off">Jordan Ellery<br>Co-Founder &amp; CEO</div>
    <div class="signature" role="img" aria-label="Handwritten signature"></div>
  </div>
  <div class="site">www.marisolquenneville.example</div>
  <div class="band">
    <svg style="left:370px" width="110" viewBox="0 0 110 7"><polygon points="7,0 55,0 48,7 0,7" fill="var(--green-deep)"/><polygon points="59,0 107,0 100,7 52,7" fill="var(--green-soft)"/></svg>
  </div>
</section>

<!-- Envelope -->
<section class="envelope">
  <svg class="flap" viewBox="0 0 508 86"><path d="M0 86 L22 12 Q26 0 40 0 L468 0 Q482 0 486 12 L508 86 Z" fill="var(--brown)"/></svg>
  <span class="brand-dot flap-dot"></span>
  <div class="sheet body">
    <div class="watermark" role="img" aria-label="Faint tree watermark"></div>
    <div class="brand">
      <span class="brand-dot"></span>
      <span class="brand-name">Marisol Quenneville, LMFT</span>
    </div>
    <div class="divider"></div>
    <div class="contact">
      <strong>Marisol Quenneville, LMFT</strong><br>
      318 Bellweather Lane, Suite 15<br>
      Palo Alto, CA 94317
      <div class="gap"></div>
      <div class="icon-row"><svg viewBox="0 0 10 10"><path d="M1 3c0-1 1-2 4-2s4 1 4 2v1H7V3H3v1H1zM2 5h6l1 4H1z"/></svg>650-555-0187</div>
      <div class="icon-row"><svg viewBox="0 0 10 10"><circle cx="5" cy="5" r="4" fill="none" stroke="var(--ink)" stroke-width="1"/><path d="M1 5h8M5 1v8" stroke="var(--ink)" stroke-width="0.8"/></svg>marisolquenneville.example</div>
    </div>
    <div class="band">
      <svg style="left:378px" width="110" viewBox="0 0 110 7"><polygon points="7,0 55,0 48,7 0,7" fill="var(--green-deep)"/><polygon points="59,0 107,0 100,7 52,7" fill="var(--green-soft)"/></svg>
    </div>
  </div>
</section>

<!-- Note cards -->
<section class="sheet card card-tent">
  <div class="brand">
    <span class="brand-dot"></span>
    <span class="brand-name">Marisol Quenneville, LMFT</span>
  </div>
  <div class="band">
    <svg style="left:122px" width="100" viewBox="0 0 100 7"><polygon points="6,0 50,0 44,7 0,7" fill="var(--green-deep)"/><polygon points="54,0 98,0 92,7 48,7" fill="var(--green-soft)"/></svg>
  </div>
</section>

<section class="sheet card card-centered">
  <div class="brand">
    <span class="brand-dot"></span>
    <span class="brand-name">Marisol Quenneville, LMFT</span>
  </div>
  <div class="site">www.marisolquenneville.example</div>
  <div class="band">
    <svg style="left:122px" width="100" viewBox="0 0 100 7"><polygon points="6,0 50,0 44,7 0,7" fill="var(--green-deep)"/><polygon points="54,0 98,0 92,7 48,7" fill="var(--green-soft)"/></svg>
  </div>
</section>

<section class="sheet card card-blank"></section>

</body>
</html>
```